HireLoopster.com needs an elegant and a professional look

We are looking for a talented Graphic Designer who will be responsible for creating compelling and innovative visual design solution for our website, www.HireLoopster.com

Thanks in advance for your interest.

Industry/Entity Type

Graphic Designer

```html
<!DOCTYPE html>
<html lang="en">
<head>
<meta charset="utf-8">
<title>HireLoopster.com – Interview Marketplace</title>
<link href="https://fonts.googleapis.com/css2?family=Open+Sans:wght@400;600&family=Arimo:wght@400&display=swap" rel="stylesheet">
<style>
:root{
  --red:#b8402e;
  --red-dark:#a8392a;
  --teal:#2e7a72;
  --teal-dark:#256a63;
  --nav:#4b4b4b;
  --ink:#222;
  --body:#444;
  --muted:#666;
  --grey-box:#555;
  --footer:#4a4a4a;
  --white:#fff;
}
*{margin:0;padding:0;box-sizing:border-box}
html,body{width:909px;height:1200px;overflow:hidden;background:var(--white)}
body{position:relative;font-family:"Open Sans",sans-serif;color:var(--ink)}
.abs{position:absolute}

.site-header{left:0;top:0;width:909px;height:95px;background:linear-gradient(#e9e9e9,#fbfbfb)}
.brand{left:130px;top:30px;display:flex;align-items:center;gap:8px}
.brand-dot{width:24px;height:24px;border-radius:50%;background:var(--teal)}
.brand-name{font-size:22px;color:var(--nav);font-weight:400;line-height:1}
.brand-tag{left:266px;top:56px;font-size:9px;color:var(--muted)}
.login{left:703px;top:38px;width:76px;height:21px;background:var(--nav);color:#fff;font-size:9px;display:flex;align-items:center}
.login-icon{width:24px;height:21px;background:var(--red);display:flex;align-items:center;justify-content:center;margin-right:10px}

.main-nav{left:0;top:95px;width:909px;height:40px;background:linear-gradient(#5a5a5a,#444)}
.nav-item{top:0;height:40px;line-height:40px;color:#fff;font-size:9.5px;text-transform:uppercase}
.nav-item.active{background:var(--red);text-align:center}
.nav-sep{top:0;width:1px;height:40px;background:#3a3a3a}
.search{left:565px;top:103px;width:190px;height:23px;background:#fff;font-size:7.5px;color:#555;padding-left:10px;line-height:23px}
.search-icon{left:766px;top:108px}

.hero{left:0;top:135px;width:909px;height:367px;background:linear-gradient(100deg,#d9cfc2 0%,#e6e2dc 35%,#cfc6bb 55%,#b49a7c 70%,#e8e2da 100%)}
.hero-title{left:339px;top:287px;width:237px;height:58px;background:rgba(70,70,70,.85);color:#fff;font-size:33px;text-align:center;line-height:58px}
.hero-arrow{top:311px;width:23px;height:23px;border-radius:50%;background:#fff;box-shadow:0 0 0 4px rgba(255,255,255,.35)}

.band-find{left:0;top:503px;width:465px;height:217px;background:linear-gradient(var(--teal),var(--teal-dark))}
.band-be{left:465px;top:503px;width:444px;height:217px;background:linear-gradient(var(--red),var(--red-dark))}
.band-person{left:365px;top:503px;width:165px;height:217px;background:linear-gradient(#3b3b3b,#1e1e1e);border-radius:60px 60px 0 0}
.band-title{top:522px;font-size:27px;color:#fff}
.perks{list-style:none;top:572px}
.perks li{height:26px;display:flex;align-items:center;gap:7px;color:#fff;font-size:9.5px}
.signin{top:661px;width:166px;height:32px;background:#f4f4f4;border:1px solid #ddd;display:flex;align-items:center;gap:8px;padding-left:10px;font-size:12.5px;color:#333}
.signin-mark{width:16px;height:16px;background:#1e7bb8}

.heading{font-size:16px;font-weight:400;color:var(--ink)}
.heading em{font-style:normal;color:var(--red)}
.welcome-copy{left:130px;top:775px;width:318px;font-family:"Arimo",sans-serif;font-size:7.6px;line-height:14.2px;color:var(--body);text-align:justify}
.read-more{left:130px;top:903px;width:65px;height:29px;background:#333;color:#fff;font-size:9.5px;border-radius:3px;text-align:center;line-height:29px}
.video{left:467px;top:779px;width:312px;height:153px;background:#222}
.video-frame{left:0;top:16px;width:312px;height:120px;background:linear-gradient(#b8b79a,#8c8a73)}
.video-url{left:7px;top:3px;color:#ddd;font-size:7px}
.video-play{left:143px;top:66px;width:27px;height:19px;background:#222;border-radius:4px}
.video-progress{left:0;top:133px;width:312px;height:3px;background:#d11}
.video-time{left:53px;top:140px;color:#ccc;font-size:6px}

.news-rule{left:130px;top:987px;width:649px;height:1px;background:#ddd}
.news-date{top:1008px;width:48px;height:80px}
.news-date-top{left:0;top:0;width:48px;height:58px;background:var(--red);color:#fff;text-align:center}
.news-day{font-size:22px;line-height:28px;padding-top:4px}
.news-month{font-size:11px}
.news-date-bottom{left:0;top:58px;width:48px;height:22px;background:var(--grey-box)}
.news-flag{left:48px;top:9px;width:0;height:0;border-top:6px solid transparent;border-bottom:6px solid transparent;border-left:8px solid var(--red)}
.news-title{font-size:12px;line-height:18px;color:#333}
.news-copy{font-family:"Arimo",sans-serif;font-size:7.6px;line-height:14.2px;color:var(--muted);width:241px;text-align:justify}

.site-footer{left:0;top:1132px;width:909px;height:68px;background:var(--footer)}
.footer-links{left:131px;top:1147px;color:#ddd;font-size:8px}
.footer-copy{left:130px;top:1171px;color:#bbb;font-size:7.5px}
.social{top:1157px;width:16px;height:16px;border-radius:50%;background:#fff}
</style>
</head>
<body>

<header class="site-header abs"></header>
<div class="brand abs"><span class="brand-dot"></span><span class="brand-name">HireLoopster.com</span></div>
<div class="brand-tag abs">Interview Marketplace</div>
<div class="login abs"><span class="login-icon"><svg width="9" height="9" viewBox="0 0 10 10"><circle cx="5" cy="3" r="2.4" fill="#fff"/><path d="M1 10a4 4 0 0 1 8 0z" fill="#fff"/></svg></span>LOG IN</div>

<nav class="main-nav abs">
  <div class="nav-item active abs" style="left:130px;width:75px">Home</div>
  <div class="nav-item abs" style="left:229px">How It Works</div>
  <div class="nav-sep abs" style="left:314px"></div>
  <div class="nav-item abs" style="left:330px">Careers</div>
  <div class="nav-sep abs" style="left:386px"></div>
  <div class="nav-item abs" style="left:401px">About Us</div>
  <div class="nav-sep abs" style="left:465px"></div>
  <div class="nav-item abs" style="left:482px">Contact Us</div>
</nav>
<div class="search abs">Search For Interviewers...</div>
<svg class="search-icon abs" width="13" height="13" viewBox="0 0 13 13"><circle cx="5.5" cy="5.5" r="4" fill="none" stroke="#fff" stroke-width="1.8"/><line x1="8.5" y1="8.5" x2="12" y2="12" stroke="#fff" stroke-width="2"/></svg>

<section class="hero abs" role="img" aria-label="Photo of a job interview with a candidate facing a panel of interviewers"></section>
<div class="hero-title abs">Hire Loopster</div>
<div class="hero-arrow abs" style="left:82px"><svg width="23" height="23" viewBox="0 0 23 23"><path d="M13 7l-4 4.5 4 4.5" fill="none" stroke="#777" stroke-width="2"/></svg></div>
<div class="hero-arrow abs" style="left:797px"><svg width="23" height="23" viewBox="0 0 23 23"><path d="M10 7l4 4.5-4 4.5" fill="none" stroke="#777" stroke-width="2"/></svg></div>

<section class="band-find abs"></section>
<section class="band-be abs"></section>
<div class="band-person abs" role="img" aria-label="Photo of a businesswoman holding a clipboard"></div>

<h2 class="band-title abs" style="left:130px;font-weight:400">Find Interviewers</h2>
<ul class="perks abs" style="left:130px">
  <li><svg width="11" height="11" viewBox="0 0 11 11"><circle cx="5.5" cy="5.5" r="5.5" fill="#fff"/><path d="M3 5.6l1.8 1.8 3.3-3.6" fill="none" stroke="#2e7a72" stroke-width="1.5"/></svg>Connect with professionals from top companies</li>
  <li><svg width="11" height="11" viewBox="0 0 11 11"><circle cx="5.5" cy="5.5" r="5.5" fill="#fff"/><path d="M3 5.6l1.8 1.8 3.3-3.6" fill="none" stroke="#2e7a72" stroke-width="1.5"/></svg>Gain interview experience with mock interviews</li>
  <li><svg width="11" height="11" viewBox="0 0 11 11"><circle cx="5.5" cy="5.5" r="5.5" fill="#fff"/><path d="M3 5.6l1.8 1.8 3.3-3.6" fill="none" stroke="#2e7a72" stroke-width="1.5"/></svg>Get feedback and share the results</li>
</ul>
<div class="signin abs" style="left:130px"><span class="signin-mark"></span>Sign In With ProNet</div>

<h2 class="band-title abs" style="left:551px;font-weight:400">Be an Interviewer</h2>
<ul class="perks abs" style="left:552px">
  <li><svg width="11" height="11" viewBox="0 0 11 11"><circle cx="5.5" cy="5.5" r="5.5" fill="#fff"/><path d="M3 5.6l1.8 1.8 3.3-3.6" fill="none" stroke="#b8402e" stroke-width="1.5"/></svg>Expand your network with new talents</li>
  <li><svg width="11" height="11" viewBox="0 0 11 11"><circle cx="5.5" cy="5.5" r="5.5" fill="#fff"/><path d="M3 5.6l1.8 1.8 3.3-3.6" fill="none" stroke="#b8402e" stroke-width="1.5"/></svg>Expand your network with new talents</li>
  <li><svg width="11" height="11" viewBox="0 0 11 11"><circle cx="5.5" cy="5.5" r="5.5" fill="#fff"/><path d="M3 5.6l1.8 1.8 3.3-3.6" fill="none" stroke="#b8402e" stroke-width="1.5"/></svg>Give feedback and promote the talents you like</li>
</ul>
<div class="signin abs" style="left:552px"><span class="signin-mark"></span>Sign In With ProNet</div>

<h3 class="heading abs" style="left:131px;top:745px">Welcome To <em>Hire Loopster</em></h3>
<p class="welcome-copy abs">Praesent vestibulum aenean nonummy hendrerit mauris. Hasellus porta. Fusce suscipit varius mi. Cum sociis natoque penatibus magnis dis parturient montes nascetur.Praesent vestibulum aenean nonummy hendrerit mauris. Hasellus porta. Fusce suscipit varius mi. Cum sociis natoque penatibus magnis dis parturient montes nascetur.Praesent vestibulum aenean nonummy hendrerit mauris. Hasellus porta. Fusce suscipit varius mi. Cum sociis natoque penatibus magnis dis parturient montes nascetur.Praesent vestibulum aenean non-ummy hendrerit mauris. Hasellus porta. Fusce suscipit varius mi. Cum sociis natoque penati-bus magnis dis parturient montes nascetur.Praesent vestibulum</p>
<div class="read-more abs">Read More</div>

<h3 class="heading abs" style="left:467px;top:745px">HOW IT WORKS</h3>
<div class="video abs">
  <div class="video-url abs">www.HireLoopster.com</div>
  <div class="video-frame abs" role="img" aria-label="Animated explainer video showing a candidate and an interviewer at their desks"></div>
  <div class="video-play abs"><svg width="27" height="19" viewBox="0 0 27 19"><path d="M11 5l7 4.5-7 4.5z" fill="#fff"/></svg></div>
  <div class="video-progress abs"></div>
  <div class="video-time abs">0:00 / 0:48</div>
</div>

<h3 class="heading abs" style="left:130px;top:959px">LATEST <em>NEWS</em></h3>
<div class="news-rule abs"></div>

<article class="abs" style="left:131px;top:1008px">
  <div class="news-date abs" style="left:0;top:0">
    <div class="news-date-top abs"><div class="news-day">15</div><div class="news-month">OCT</div></div>
    <div class="news-flag abs"></div>
    <div class="news-date-bottom abs"></div>
  </div>
</article>
<div class="news-title abs" style="left:203px;top:1005px">At vero eos et accusamus et iusto<br>Morbi tempor quam</div>
<p class="news-copy abs" style="left:204px;top:1050px">Morbi tempor quam vel massa adi piscing ute cursus mi congue pelle ntesque niselit er comte modo. velultrices vel, conseq. Morbi tempor quam vel massa adi piscing ute cursus mi congue pelle ntesque niselit er comte</p>

<article class="abs" style="left:466px;top:1008px">
  <div class="news-date abs" style="left:0;top:0">
    <div class="news-date-top abs"><div class="news-day">15</div><div class="news-month">OCT</div></div>
    <div class="news-flag abs"></div>
    <div class="news-date-bottom abs"></div>
  </div>
</article>
<div class="news-title abs" style="left:538px;top:1005px">At vero eos et accusamus et iusto<br>Morbi tempor quam</div>
<p class="news-copy abs" style="left:539px;top:1050px">Morbi tempor quam vel massa adi piscing ute cursus mi congue pelle ntesque niselit er comte modo. velultrices vel, conseq. Morbi tempor quam vel massa adi piscing ute cursus mi congue pelle ntesque niselit er comte</p>

<footer class="site-footer abs"></footer>
<div class="footer-links abs">Home &nbsp;| &nbsp;The Opportunity &nbsp;| &nbsp;About Us &nbsp;| &nbsp;Contact Us</div>
<div class="footer-copy abs">©2014 Hire Loopster, All Rights Reserved.</div>
<div class="social abs" style="left:629px"></div>
<div class="social abs" style="left:651px"></div>
<div class="social abs" style="left:673px"></div>
<div class="social abs" style="left:695px"></div>

</body>
</html>
```